K&T Holdings

Design a modern simple business card. I have attached a clean version of a card we like form Marrowfield Partners another company we own. I also attached the old K&T card design and logo and a couple of ideas we had but just can't finalize on whether we like them or not. We would like to include the 20 year logo somewhere on the card.

```html
<!DOCTYPE html>
<html lang="en">
<head>
<meta charset="utf-8">
<title>K&amp;T Holdings Business Card</title>
<link href="https://fonts.googleapis.com/css2?family=Open+Sans:ital,wght@0,400;0,700;0,800;1,400&display=swap" rel="stylesheet">
<style>
  :root {
    --navy: #24206a;
    --navy-text: #27236e;
    --white: #ffffff;
    --grey-text: #6b6b6b;
    --stage: #2b2b2d;
    --rule-light: rgba(255,255,255,0.55);
  }
  * { box-sizing: border-box; margin: 0; padding: 0; }
  html, body { width: 1200px; height: 900px; overflow: hidden; }
  body {
    background: var(--stage);
    font-family: "Open Sans", Arial, sans-serif;
    display: flex; flex-direction: column; align-items: center; justify-content: center; gap: 40px;
  }
  .card { width: 700px; height: 400px; position: relative; overflow: hidden; }

  /* Front */
  .card-front { background: var(--white); color: var(--navy-text); }
  .person { position: absolute; left: 48px; top: 52px; }
  .person-name { font-size: 27px; font-weight: 800; letter-spacing: 1px; text-transform: uppercase; }
  .person-title { font-size: 17px; font-style: italic; color: var(--grey-text); margin-top: 2px; }
  .front-rule { position: absolute; left: 48px; right: 48px; top: 140px; height: 1.5px; background: var(--navy); }
  .contact-list { position: absolute; left: 48px; top: 158px; list-style: none; color: var(--grey-text); font-size: 17px; line-height: 27px; }
  .contact-list li { display: flex; align-items: center; gap: 10px; }
  .contact-list svg { width: 14px; height: 14px; fill: var(--navy); flex: none; }
  .front-brand { position: absolute; right: 56px; top: 180px; display: flex; align-items: center; gap: 14px; }
  .brand-dot { width: 30px; height: 30px; border-radius: 50%; background: var(--navy); flex: none; }
  .brand-name { font-size: 30px; font-weight: 800; color: var(--navy-text); white-space: nowrap; }
  .address { position: absolute; right: 48px; bottom: 40px; text-align: right; font-size: 17px; line-height: 25px; color: var(--grey-text); }

  /* Back */
  .card-back { background: var(--navy); color: var(--white); }
  .back-brand { position: absolute; left: 44px; top: 116px; display: flex; align-items: center; gap: 12px; }
  .back-brand .brand-dot { background: var(--white); width: 28px; height: 28px; }
  .back-brand .brand-name { color: var(--white); font-size: 34px; }
  .back-divider { position: absolute; left: 385px; top: 50px; width: 1px; height: 190px; background: var(--rule-light); transform: rotate(18deg); }
  .anniversary { position: absolute; left: 430px; top: 62px; text-align: center; width: 220px; }
  .anniversary-number { font-size: 96px; font-weight: 800; line-height: 1; white-space: nowrap; }
  .anniversary-number small { font-size: 22px; letter-spacing: 2px; vertical-align: 40px; margin-left: 4px; }
  .anniversary-years { font-size: 30px; letter-spacing: 4px; margin-top: 4px; }
  .services { position: absolute; left: 0; right: 0; bottom: 52px; text-align: center; }
  .services-heading { font-size: 21px; font-weight: 800; letter-spacing: 1px; text-transform: uppercase; }
  .services-list { font-size: 16px; margin-top: 8px; }
</style>
</head>
<body>
  <section class="card card-front" aria-label="Business card front">
    <div class="person">
      <div class="person-name">Dana Whitfield</div>
      <div class="person-title">IT Director</div>
    </div>
    <div class="front-rule"></div>
    <ul class="contact-list">
      <li><svg viewBox="0 0 24 24"><path d="M6.6 10.8a15.1 15.1 0 0 0 6.6 6.6l2.2-2.2c.3-.3.7-.4 1-.2 1.1.4 2.3.6 3.6.6.6 0 1 .4 1 1V20c0 .6-.4 1-1 1A17 17 0 0 1 3 4c0-.6.4-1 1-1h3.5c.6 0 1 .4 1 1 0 1.3.2 2.5.6 3.6.1.3 0 .7-.2 1z"/></svg>409-555-0147</li>
      <li><svg viewBox="0 0 24 24"><path d="M7 1h10a2 2 0 0 1 2 2v18a2 2 0 0 1-2 2H7a2 2 0 0 1-2-2V3a2 2 0 0 1 2-2zm0 3v15h10V4z"/></svg>409-555-0183</li>
      <li><svg viewBox="0 0 24 24"><path d="M2 5h20v14H2zm2 2v.5l8 5 8-5V7z"/></svg>dwhitfield@ktholdings.com</li>
      <li><svg viewBox="0 0 24 24"><circle cx="12" cy="12" r="10"/></svg>www.ktholdings.com</li>
    </ul>
    <div class="front-brand">
      <span class="brand-dot"></span>
      <span class="brand-name">K&amp;T Holdings</span>
    </div>
    <div class="address">418 Cedar Avenue, Suite 204<br>Port Arthur, TX 77640</div>
  </section>

  <section class="card card-back" aria-label="Business card back">
    <div class="back-brand">
      <span class="brand-dot"></span>
      <span class="brand-name">K&amp;T Holdings</span>
    </div>
    <div class="back-divider"></div>
    <div class="anniversary">
      <div class="anniversary-number">20<small>YEARS</small></div>
      <div class="anniversary-years">2005-2025</div>
    </div>
    <div class="services">
      <div class="services-heading">Complete Plant Support Services</div>
      <div class="services-list">Piping/Structural • Electrical • Welding • Pumps &amp; Valves • Exchanger Repair</div>
    </div>
  </section>
</body>
</html>
```